Stationery Design Project for Holloway Kenbukan Karate Studio

We Need a Stationery Design for a Karate School Teaching Okinawa Shorin Ryu Karate in Marlow Springs, Florida, U.S.A.

Target Market(s)

Adults Base Western Speaking aged between 25 and 65 yrs, old that handle household budgets

Industry/Entity Type

School

Requirements
Must have
• Name of business: Holloway Kenbukan Karate Studio
Address: Larkspur Commons 18342 US Hwy. 91
Marlow Springs, Florida. 33914
Phone # : 407-555-0183
email : Hollowaykenbukanstudio@mailgrove.example
Logo - attatched

```html
<!DOCTYPE html>
<html lang="en">
<head>
<meta charset="utf-8">
<title>Holloway Kenbukan Karate Studio – Business Card</title>
<link rel="stylesheet" href="https://fonts.googleapis.com/css2?family=PT+Sans:ital@1&family=Tenor+Sans&display=swap">
<style>
  :root {
    --card-white: #ffffff;
    --card-red: #fe0a00;
    --accent-gold: #d3c65c;
    --name-grey: #5f5f5f;
    --mark-ink: #1a1a1a;
    --edge-grey: #b5b5b5;
    --text-light: #ffffff;
  }
  html, body {
    margin: 0;
    padding: 0;
    width: 1200px;
    height: 777px;
    overflow: hidden;
    background: var(--card-white);
  }
  .card {
    position: relative;
    width: 1200px;
    height: 777px;
    box-sizing: border-box;
    border: 2px solid var(--edge-grey);
    background: var(--card-white);
    overflow: hidden;
    font-family: "Tenor Sans", sans-serif;
  }
  .card__band {
    position: absolute;
    left: 0;
    top: 320px;
    width: 100%;
    height: 457px;
    background: var(--card-red);
  }
  .person {
    position: absolute;
    right: 603px;
    top: 110px;
    text-align: right;
  }
  .person__name {
    margin: 0;
    font-family: "PT Sans", sans-serif;
    font-style: italic;
    font-size: 42px;
    line-height: 1;
    color: var(--name-grey);
  }
  .person__role {
    margin: 14px 0 0;
    font-size: 28px;
    line-height: 1;
    letter-spacing: 0.5px;
    color: var(--card-red);
  }
  .brand-mark {
    position: absolute;
    left: 960px;
    top: 78px;
    width: 176px;
    text-align: center;
  }
  .brand-mark__dot {
    display: block;
    width: 62px;
    height: 62px;
    margin: 0 auto 16px;
    border-radius: 50%;
    background: var(--card-red);
  }
  .brand-mark__name {
    margin: 0;
    font-size: 24px;
    line-height: 1.12;
    letter-spacing: 0.5px;
    text-transform: uppercase;
    color: var(--mark-ink);
  }
  .accent-tab {
    position: absolute;
    left: 68px;
    top: 340px;
    width: 72px;
    height: 116px;
  }
  .studio {
    position: absolute;
    right: 70px;
    top: 372px;
    text-align: right;
    color: var(--text-light);
  }
  .studio__name {
    margin: 0 0 14px;
    font-size: 35px;
    font-weight: 400;
    line-height: 1.2;
    letter-spacing: 2.6px;
    text-transform: uppercase;
    color: var(--accent-gold);
  }
  .studio__address,
  .studio__contact {
    margin: 0;
    font-style: normal;
    font-size: 40px;
    line-height: 53px;
    letter-spacing: 0.6px;
  }
  .studio__contact {
    margin-top: 50px;
  }
  .studio__contact span {
    display: block;
  }
</style>
</head>
<body>
  <main class="card">
    <section class="person">
      <p class="person__name">Sensei Marcus T. Reyes</p>
      <p class="person__role">INSTRUCTOR</p>
    </section>

    <div class="brand-mark">
      <span class="brand-mark__dot"></span>
      <p class="brand-mark__name">Holloway<br>Kenbukan<br>Karate</p>
    </div>

    <div class="card__band"></div>

    <svg class="accent-tab" viewBox="0 0 72 116" aria-hidden="true">
      <path d="M0 0 H14 A58 58 0 0 1 14 116 H0 Z" fill="var(--accent-gold)"/>
    </svg>

    <section class="studio">
      <h1 class="studio__name">Holloway Kenbukan Karate Studio</h1>
      <address class="studio__address">
        Larkspur Commons 18342 US Hwy. 91<br>
        Marlow Springs, Florida. 33914
      </address>
      <p class="studio__contact">
        <span>Phone: 407-555-0183</span>
        <span>email: Hollowaykenbukanstudio@mailgrove.example</span>
      </p>
    </section>
  </main>
</body>
</html>
```